Marijuana Lifestyle Multi-Shop Brand Website

We need a website that provides an online retail shop for our products, along with the additional functionality:

Main Page: Slider with great photography (we are still looking for a professional photographer to take photos for us.

Shop Tab: E-commerce site.
- Main Categories:
- Accessories
- Bubblers
- Dry Pieces
- Scientific Glass
- Water Pipes
- Custom Shop
- University Store

Stores/Resellers: This is a store look-up, so people can enter their zipcode and find our resellers and partners.

Brand Partners: Just a basic filter and page so that we can highlight our partners and why we've selected them.

Contact Us: Basic Form
- Career Page: Basic Page

About Us: Basic Page

Blog:

Search Bar:

Essentially, we want a near exact copy of this website, but with our brand, logo and content. https://corkwillowbins.com/

This site is really really simple, but we like simple.

Our reserved domain address is: www.runbaketend.com

About Us:
We are multi-shop for marijuana-related accessories. We sell quality glass pipes, vaporizers, amazing storage options, dime bags, custom t-shirts and other stuff.

We have a network of resellers that allow us to put in micro-installations into gift shops, convenience stores, tobacco stores, etc. and we are trying to change the overall perception that buying these items should be mainstream and as transparent as going to the Fen or the Walnut Shop.

I've attached a logo that should give you an idea of our color scheme. We don't have our photography yet for the slider
Updates

As an FYI, for the e-commerce part of my website, I already have a license for WP SwiftTill.

Industry/Entity Type

Shop

```html
<!DOCTYPE html>
<html lang="en">
<head>
<meta charset="utf-8">
<title>Fernloft — Find Your New Look</title>
<link rel="stylesheet" href="https://fonts.googleapis.com/css2?family=Josefin+Sans:wght@300;400&family=Open+Sans:wght@400;600;700&display=swap">
<style>
  :root {
    --header-bg: #1b110e;
    --hero-dark: #6e3a30;
    --hero-mid: #8e5344;
    --hero-light: #a66b59;
    --strip-bg: #120c0a;
    --strip-border: #6d6a3e;
    --category-bg: #1d130f;
    --footer-bg: #050404;
    --accent: #c5d08a;
    --accent-dark: #a9b46c;
    --nav-text: #9b9690;
    --white: #ffffff;
    --footer-link: #7c7670;
    --footer-copy: #5f5a55;
    --icon-grey: #4a4745;
    --social-blue: #2c5fa8;
  }
  * { box-sizing: border-box; margin: 0; padding: 0; }
  html, body { width: 1200px; height: 801px; overflow: hidden; background: var(--footer-bg); }
  body { font-family: "Open Sans", Arial, sans-serif; position: relative; }

  .site-header { position: absolute; left: 0; top: 0; width: 1200px; height: 100px; background: var(--header-bg); z-index: 3; }
  .brand { position: absolute; left: 122px; top: 28px; display: flex; align-items: center; gap: 12px; }
  .brand-mark { width: 44px; height: 44px; border-radius: 50%; background: var(--accent-dark); }
  .brand-name { font-weight: 700; font-size: 22px; color: var(--accent); }

  .main-nav a { position: absolute; top: 38px; font-size: 17px; font-weight: 600; color: var(--nav-text); text-decoration: none; }
  .main-nav a.is-active { color: var(--white); }

  .header-tools svg { position: absolute; }
  .close-button { position: absolute; left: 1024px; top: 31px; width: 41px; height: 41px; border-radius: 50%; background: var(--accent); }

  .search-box { position: absolute; left: 784px; top: 80px; width: 266px; height: 45px; border: 2px solid var(--accent); background: #1e1916; z-index: 4; }
  .search-input { position: absolute; left: 6px; top: 6px; width: 216px; height: 29px; background: #3b3836; }
  .search-button { position: absolute; left: 224px; top: 6px; width: 32px; height: 29px; background: var(--accent); }

  .hero { position: absolute; left: 0; top: 100px; width: 1200px; height: 525px;
    background: radial-gradient(ellipse at 70% 40%, var(--hero-light) 0%, var(--hero-mid) 45%, var(--hero-dark) 100%); overflow: hidden; }
  .hero-photo { position: absolute; left: 70px; top: 0; width: 480px; height: 525px;
    background: radial-gradient(ellipse at 50% 45%, #b07a5e 0%, #8b5a44 45%, rgba(110,58,48,0) 75%); }
  .hero-title { position: absolute; left: 594px; top: 92px; font-family: "Josefin Sans", Arial, sans-serif; font-weight: 300;
    font-size: 66px; line-height: 68px; letter-spacing: 4px; color: var(--accent); }
  .hero-text { position: absolute; left: 600px; top: 266px; width: 470px; font-size: 15.5px; line-height: 24px; font-weight: 700; color: var(--white); }
  .slider-dots { position: absolute; left: 1079px; top: 216px; display: flex; flex-direction: column; gap: 9px; }
  .slider-dots span { width: 14px; height: 14px; border-radius: 50%; border: 1.5px solid var(--white); }
  .slider-dots span.is-current { background: var(--white); }

  .thumb-strip { position: absolute; left: 133px; top: 461px; width: 934px; height: 164px; background: var(--strip-bg); border: 1px solid var(--strip-border); border-bottom: none; z-index: 2; }
  .thumb { position: absolute; top: 18px; width: 203px; height: 125px; border: 2px solid #4d4a46; }
  .thumb-1 { left: 31px; background: linear-gradient(135deg, #3a2019, #8a4a3a 60%, #c98a6e); }
  .thumb-2 { left: 254px; background: linear-gradient(135deg, #2a2418, #6b5633 55%, #a08856); }
  .thumb-3 { left: 475px; background: linear-gradient(135deg, #4a3a2c, #8a6a50 55%, #2e2620); }
  .thumb-4 { left: 698px; background: linear-gradient(135deg, #d7a149, #c98a3a 50%, #8c5a2a); }
  .strip-arrow { position: absolute; top: 516px; z-index: 3; }

  .category-bar { position: absolute; left: 0; top: 625px; width: 1200px; height: 44px; background: var(--category-bg); }
  .category-bar a { position: absolute; top: 11px; font-size: 15.5px; font-weight: 600; color: var(--white); text-decoration: none; }
  .category-bar a.is-active { left: 133px; top: 0; width: 119px; height: 44px; background: var(--accent); color: #2a2a1c; font-weight: 400; text-align: center; line-height: 44px; }

  .site-footer { position: absolute; left: 0; top: 669px; width: 1200px; height: 132px; background: var(--footer-bg); }
  .social-links { position: absolute; left: 490px; top: 18px; display: flex; gap: 8px; }
  .social-links span { width: 30px; height: 30px; background: var(--icon-grey); }
  .social-links span:first-child { background: var(--social-blue); }
  .footer-nav { position: absolute; left: 0; top: 66px; width: 1200px; text-align: center; font-size: 13px; color: var(--footer-link); }
  .footer-nav a { color: var(--footer-link); text-decoration: none; }
  .footer-nav a.is-active { color: var(--accent); }
  .footer-nav .sep { margin: 0 6px; }
  .copyright { position: absolute; left: 0; top: 96px; width: 1200px; text-align: center; font-size: 12px; color: var(--footer-copy); }
</style>
</head>
<body>
  <header class="site-header">
    <div class="brand"><span class="brand-mark"></span><span class="brand-name">Fernloft</span></div>
    <nav class="main-nav">
      <a class="is-active" style="left:277px">Home</a>
      <a style="left:371px">About Us</a>
      <a style="left:490px">Service</a>
      <a style="left:592px">Shop</a>
      <a style="left:678px">Blog</a>
      <a style="left:759px">Contact</a>
    </nav>
    <div class="header-tools">
      <svg style="left:922px;top:37px" width="28" height="26" viewBox="0 0 28 26" aria-label="Account">
        <circle cx="11" cy="8" r="6" fill="#8a8580"/>
        <path d="M0 25c0-7 5-10 11-10s11 3 11 10z" fill="#8a8580"/>
        <path d="M22 15v8M18 19h8" stroke="#8a8580" stroke-width="2.5"/>
      </svg>
      <svg style="left:978px;top:36px" width="32" height="28" viewBox="0 0 32 28" aria-label="Cart">
        <path d="M1 4h5l4 14h16l3-10H8" fill="none" stroke="#8a8580" stroke-width="2.5"/>
        <circle cx="12" cy="24" r="2.5" fill="#8a8580"/><circle cx="24" cy="24" r="2.5" fill="#8a8580"/>
        <path d="M17 2v9M13 7l4 4 4-4" fill="none" stroke="#8a8580" stroke-width="2"/>
      </svg>
      <div class="close-button">
        <svg width="41" height="41" viewBox="0 0 41 41" aria-label="Close search"><path d="M14 14l13 13M27 14L14 27" stroke="#1b110e" stroke-width="2.5"/></svg>
      </div>
    </div>
  </header>

  <div class="search-box">
    <div class="search-input"></div>
    <div class="search-button">
      <svg width="32" height="29" viewBox="0 0 32 29" aria-label="Search"><circle cx="14" cy="13" r="6" fill="none" stroke="#1b110e" stroke-width="2.5"/><path d="M18.5 17.5l5 5" stroke="#1b110e" stroke-width="3"/></svg>
    </div>
  </div>

  <section class="hero">
    <div class="hero-photo" role="img" aria-label="Slider photograph: model in a fur-trimmed jacket wearing a bold gold necklace"></div>
    <h1 class="hero-title">FIND YOUR<br>NEW LOOK</h1>
    <p class="hero-text">Dignissim non fermentum nec, rutrum vitae nunc. Vesti Bulum laoreet nisi acdignissim non fermentum nec rutr Umvitae nunc.</p>
    <div class="slider-dots"><span class="is-current"></span><span></span><span></span><span></span><span></span></div>
  </section>

  <div class="thumb-strip">
    <div class="thumb thumb-1" role="img" aria-label="Thumbnail: hands with red nails and earrings"></div>
    <div class="thumb thumb-2" role="img" aria-label="Thumbnail: jewellery on a gold patterned background"></div>
    <div class="thumb thumb-3" role="img" aria-label="Thumbnail: hands wearing rings and bracelets"></div>
    <div class="thumb thumb-4" role="img" aria-label="Thumbnail: gold rings on a warm amber background"></div>
  </div>
  <svg class="strip-arrow" style="left:122px" width="22" height="36" viewBox="0 0 22 36" aria-label="Previous"><path d="M20 2L4 18l16 16" fill="none" stroke="#fff" stroke-width="4"/></svg>
  <svg class="strip-arrow" style="left:1055px" width="22" height="36" viewBox="0 0 22 36" aria-label="Next"><path d="M2 2l16 16L2 34" fill="none" stroke="#fff" stroke-width="4"/></svg>

  <nav class="category-bar">
    <a class="is-active">Accessories</a>
    <a style="left:282px">Bubblers</a>
    <a style="left:393px">Dry Pieces</a>
    <a style="left:513px">Scientific Glass</a>
    <a style="left:664px">Water Pipes</a>
    <a style="left:796px">Custom Shop</a>
    <a style="left:936px">University Store</a>
  </nav>

  <footer class="site-footer">
    <div class="social-links" aria-label="Social links"><span></span><span></span><span></span><span></span><span></span><span></span></div>
    <p class="footer-nav">
      <a class="is-active">Home</a><span class="sep">/</span><a>About Us</a><span class="sep">/</span><a>Products</a><span class="sep">/</span><a>Shop</a><span class="sep">/</span><a>Collection</a><span class="sep">/</span><a>Blog</a><span class="sep">/</span><a>Checkout My Account</a><span class="sep">/</span><a>Register</a><span class="sep">/</span><a>Contact Us</a>
    </p>
    <p class="copyright">Copyright © 2014 Fernloft. All rights reserved.</p>
  </footer>
</body>
</html>
```